Zielgruppe
IT Dienstleistungen, Hardware- u. Softwarevertrieb, Consulting, Sicherheitssysteme
Meine Zielgruppe sind Geschäftskunden (B2B) - Kleine bis mittelständische Unternehmen
Aufgabenstellung
Verschiedene Buttons, wie z.B. Partnernetzwerk, Wir über uns, Aktuelle Angebote, Zertifikate. Die Seite gibt kreativen Spielraum und ist an keinerlei Vorgabe gebunden - Innovatives und modernes Design sind willkommen (darf ruhig mal außergewöhlich sein). Logo ist vorhanden und sollte eingebaut werden (siehe Upload). Anregungen können ebenfalls der Landing Page entnommen werden. Zudem fände ich es gut, wenn einige bewegliche Bilder auf der Seite eingebaut würden und die rote Farbe des Hutes im Layout auftaucht (wenn möglich).

```html
<!DOCTYPE html>
<html lang="de">
<head>
<meta charset="utf-8">
<title>Korvan – IT-Dienstleistungen</title>
<link href="https://fonts.googleapis.com/css2?family=Open+Sans:wght@300;400;600;700&display=swap" rel="stylesheet">
<style>
:root{
  --bg:#1c1c1c;
  --red:#d0232a;
  --red-dark:#7a0d1e;
  --navy:#141a2c;
  --light:#f4f4f4;
  --white:#ffffff;
  --grey:#595959;
  --grey-dark:#3a3a3a;
  --footer:#2d2d2d;
  --text:#333333;
  --muted:#666666;
  --badge:#1c8fd1;
}
*{box-sizing:border-box;margin:0;padding:0}
html,body{width:1003px;height:1200px;overflow:hidden;background:var(--bg);font-family:"Open Sans",Arial,sans-serif;color:var(--text)}
.page{position:absolute;top:51px;width:304px;overflow:hidden}
.page-home{left:191px;height:1060px;background:var(--white)}
.page-about{left:503px;height:870px;background:var(--light)}
.abs{position:absolute}

.topbar{left:0;top:0;width:304px;height:63px;background:var(--red);color:var(--white);text-align:center;font-size:7px}
.topbar .line{position:absolute;left:0;right:0}
.offer-btn{position:absolute;left:85px;top:35px;width:163px;height:20px;background:var(--red-dark);font-weight:700;font-size:7px;line-height:20px}
.header{left:0;top:63px;width:304px;height:43px;background:#f7f7f7}
.brand-dot{left:10px;top:11px;width:21px;height:21px;border-radius:50%;background:var(--red)}
.brand-name{left:38px;top:12px;font-size:15px;color:var(--red);font-weight:400;line-height:1}
.burger{right:10px;top:15px;width:16px}
.burger span{display:block;height:3px;background:var(--red);border-radius:2px;margin-bottom:2.5px}

.hero{left:0;top:106px;width:304px;height:171px;background:linear-gradient(135deg,#23304a,var(--navy) 60%,#0c0f1a)}
.hero-art{left:2px;top:20px;width:150px;height:118px;border-radius:40% 40% 50% 50%;background:radial-gradient(circle at 45% 45%,#e9a45a,#9a5a2c 60%,#2a3550)}
.hero h1{left:154px;top:48px;font-size:17px;color:var(--white);font-weight:400}
.hero p{left:154px;top:76px;width:145px;font-size:5.6px;line-height:9.5px;color:var(--white)}
.btn-red{background:var(--red);color:var(--white);font-size:7px;text-align:center}
.hero .btn-red{left:154px;top:109px;width:66px;height:16px;line-height:16px}

.band{left:0;top:277px;width:304px;height:43px;background:var(--red);color:var(--white)}
.band p{left:4px;top:13px;font-size:7.2px;line-height:9px;font-weight:300}
.band .outline{left:218px;top:14px;width:81px;height:14px;border:1px solid var(--white);font-size:5px;font-weight:700;text-align:center;line-height:12px}
.notch{left:146px;top:320px;width:0;height:0;border-left:5px solid transparent;border-right:5px solid transparent;border-top:5px solid var(--red)}

.features{left:0;top:320px;width:304px;height:387px;background:var(--light)}
.feature-img{left:8px;width:145px;height:96px}
.tag{left:4px;width:45px;height:12px;background:var(--red);color:var(--white);font-size:4.5px;line-height:12px;text-align:center}
.feature-title{left:158px;font-size:7.5px;color:var(--red);font-weight:600}
.feature-text{left:158px;width:140px;font-size:5.3px;line-height:8.5px;color:var(--muted)}

.service-title{left:14px;top:726px;font-size:12.5px;color:var(--red);font-weight:700}
.service-dots{left:0;top:732px;font-size:6px;color:#bbb;letter-spacing:1px}
.card{width:144px;background:#efefef}
.card .img{width:144px;height:82px}
.card h3{margin:5px 0 0 7px;font-size:8.5px;font-weight:400;color:#444}
.card p{margin:3px 7px 0;font-size:4.5px;line-height:8.5px;color:var(--muted)}

.about-rule{left:5px;top:23px;width:20px;height:1px;background:#bbb}
.about-h{left:5px;top:30px;font-size:15px;color:#333;line-height:19px;font-weight:300}
.about-h b{font-weight:700}
.about-lead{left:5px;top:74px;width:296px;font-size:5.7px;line-height:7.5px;font-weight:700;color:#222}
.about-text{left:5px;top:103px;width:172px;font-size:5.2px;line-height:6.8px;color:#333}
.divider{left:0;top:227px;width:304px;height:2px;background:#cfcfcf}
.step{width:148px;height:134px;color:var(--white);text-align:center}
.step h4{font-size:12px;font-weight:400;margin-top:6px}
.step p{font-size:6.3px;line-height:11px;margin:6px 8px 0}
.step svg{margin-top:22px}
.step-intro{text-align:left;padding:12px 11px}
.step-intro h4{font-size:12.5px;line-height:14px;margin:0}
.step-intro h4 b{font-size:15px;font-weight:700}
.step-intro p{margin:10px 0 0;text-align:left}
.step-intro .more{font-size:4.8px;font-weight:700;margin-top:11px}

.partners-label{left:8px;top:598px;font-size:5.3px;line-height:8.5px;color:#555}
.partners{left:92px;top:543px;width:197px;height:78px;background:var(--white)}
.badge{position:absolute;width:52px;height:26px;background:var(--badge)}

.contact{left:0;top:631px;width:304px;height:239px;background:var(--footer);color:var(--white)}
.contact h5{position:absolute;left:4px;top:20px;font-size:6.3px;font-weight:600}
.field{position:absolute;height:15px;background:#e0e0e0;color:#777;font-size:5.6px;padding:4px 6px}
.send{left:252px;top:115px;width:47px;height:16px;line-height:16px;font-weight:700;font-size:6px}
.foot-col{position:absolute;font-size:5px;line-height:7px}
.foot-nav{position:absolute;left:110px;top:132px;font-size:6px;line-height:14.5px}
.foot-bar{position:absolute;left:0;top:211px;width:304px;height:2px;background:#444}
.copy{position:absolute;left:5px;top:222px;font-size:4.5px;color:#aaa}
.copy b{color:var(--white);font-weight:400}
.social{position:absolute;right:8px;top:221px;display:flex;gap:11px}
.social i{display:block;width:5px;height:5px;border-radius:50%;background:var(--white)}
</style>
</head>
<body>

<section class="page page-home">
  <div class="abs topbar">
    <div class="line" style="top:6px">
      <svg width="5" height="7" viewBox="0 0 10 14"><path d="M5 0a5 5 0 0 0-5 5c0 4 5 9 5 9s5-5 5-9a5 5 0 0 0-5-5zm0 7a2 2 0 1 1 0-4 2 2 0 0 1 0 4z" fill="#fff"/></svg>
      Geschäftsführer: Lukas Brenner Lindenweg 7 DE-59100 Talheim</div>
    <div class="line" style="top:20px">
      <svg width="6" height="6" viewBox="0 0 12 12"><path d="M2 0l2.5 2.5-1.3 1.8a7 7 0 0 0 4.5 4.5l1.8-1.3L12 10l-2 2C4 12 0 8 0 2z" fill="#fff"/></svg>
      0 (+49) 1234 / 5678-90</div>
    <div class="offer-btn">GERNE ERSTELLE ICH IHNEN EIN ANGEBOT</div>
  </div>

  <header class="abs header">
    <div class="abs brand-dot"></div>
    <div class="abs brand-name">Korvan</div>
    <div class="abs burger"><span></span><span></span><span></span></div>
  </header>

  <div class="abs hero">
    <div class="abs hero-art" role="img" aria-label="Digitales Schild mit Schlüsselloch auf Datenhintergrund"></div>
    <h1 class="abs">SICHERHEIT</h1>
    <p class="abs">Da neue Sicherheitsbedrohungen ständig entstehen muss der Schutz Ihres Unternehmensnetzes, Daten und Systeme oberste Priorität haben</p>
    <div class="abs btn-red">JETZT ZITIEREN</div>
  </div>

  <div class="abs band">
    <p class="abs">Die führende Software, Hardware und Managed<br>IT Services Provider</p>
    <div class="abs outline">KOSTENLOSE BERATUNG</div>
  </div>
  <div class="abs notch"></div>

  <div class="abs features">
    <div class="abs feature-img" style="top:28px;background:linear-gradient(90deg,#8fa3b3,#c8d3dc 45%,#c4333a 80%,#e9e2da)" role="img" aria-label="Mitarbeiterin am Computerarbeitsplatz"></div>
    <div class="abs tag" style="top:105px">WEITER LESEN +</div>
    <div class="abs feature-title" style="top:29px">Individuelle IT-Lösung</div>
    <div class="abs feature-text" style="top:45px">Wir planen und realisieren für Sie ausschließlich maßgeschneiderte und flexible IT-Lösungen.</div>

    <div class="abs feature-img" style="top:145px;background:linear-gradient(120deg,#dfe3e6,#7a8796 40%,#1f2a44 70%,#c9ced4)" role="img" aria-label="Geschäftsmann zeichnet einen roten Aufwärtspfeil"></div>
    <div class="abs tag" style="top:222px">WEITER LESEN +</div>
    <div class="abs feature-title" style="top:146px">Lokale Partner</div>
    <div class="abs feature-text" style="top:162px">Als lokaler Partner sind wir jederzeit für Sie erreich-bar und zeitnah vor Ort.</div>

    <div class="abs feature-img" style="top:262px;background:linear-gradient(90deg,#c98c63,#e8c2a0 40%,#4a8fc1 75%,#e5e8ea)" role="img" aria-label="Gruppe junger Menschen mit Daumen nach oben"></div>
    <div class="abs tag" style="top:339px">WEITER LESEN +</div>
    <div class="abs feature-title" style="top:263px">Engagiert und Qualifiziert</div>
    <div class="abs feature-text" style="top:279px">Durch unsere langjährige Erfahrung können wir Ihnen fundiertes Know-How bieten.</div>
  </div>

  <div class="abs service-dots">•••</div>
  <h2 class="abs service-title">UNSER SERVICE</h2>

  <div class="abs card" style="left:2px;top:762px;height:130px">
    <div class="img" style="background:linear-gradient(135deg,#1c2b12,#6a7a2a 50%,#2a2a1c)" role="img" aria-label="Nahaufnahme einer Computerplatine"></div>
    <h3>Hardware</h3>
    <p>Lorem ipsum dolor sit amet, consectetur adipiscing elit. Sed cursus sollicitudin odio, eu tempor velit pellen-tesque et.</p>
  </div>
  <div class="abs card" style="left:159px;top:762px;height:130px">
    <div class="img" style="background:linear-gradient(135deg,#101a3a,#2a3a7a 50%,#4a2a5a)" role="img" aria-label="Bunter Programmcode auf dunklem Bildschirm"></div>
    <h3>Software</h3>
    <p>Lorem ipsum dolor sit amet, consectetur adipiscing elit. Sed cursus sollicitudin odio, eu tempor velit pellen-tesque et.</p>
  </div>
  <div class="abs card" style="left:73px;top:906px;height:130px">
    <div class="img" style="background:linear-gradient(90deg,#1c4a6a,#3a8ab0 35%,#b52a2a 55%,#3a8ab0 75%,#1c3a5a)" role="img" aria-label="Reihe digitaler Vorhängeschlösser, eines rot geöffnet"></div>
    <h3>Sicherheit</h3>
    <p>Lorem ipsum dolor sit amet, consectetur adipiscing elit. Sed cursus sollicitudin odio, eu tempor velit pellen-tesque et.</p>
  </div>
</section>

<section class="page page-about">
  <div class="abs about-rule"></div>
  <h2 class="abs about-h">WER WIR SIND<br><b>WARUM WÄHLE MICH</b></h2>
  <p class="abs about-lead">Lorem ipsum dolor sit amet, consectetur adipiscing elit, sed do eiusmod tempor incididunt ut labore et dolore magna aliqua. Ut enim ad minim veniam, quis nostrud exercitation ullamco laboris nisi ut aliquip ex ea commodo consequat.</p>
  <p class="abs about-text">Duis aute irure dolor in reprehenderit in voluptate velit esse cillum dolore eu fugiat nulla pariatur. Excepteur sint occaecat cupidatat non proident, sunt in culpa qui officia deserunt mollit anim id est laborum. Sed ut perspiciatis unde omnis iste natus error sit voluptatem accusantium doloremque laudantium, totam rem aperiam, eaque ipsa quae ab illo inventore veritatis et quasi architecto beatae vitae dicta sunt explicabo. Nemo enim ipsam voluptatem quia voluptas sit aspernatur aut odit aut fugit, sed quia consequuntur magni dolores eos qui ratione voluptatem sequi nesciunt.<br><br>Neque porro quisquam est, qui dolorem ipsum quia dolor sit amet, consectetur, adipisci velit, sed quia non numquam eius modi tempora incidunt ut labore et dolore magnam aliquam quaerat voluptatem.</p>
  <div class="abs divider"></div>

  <div class="abs step step-intro" style="left:4px;top:245px;background:var(--red)">
    <h4>Unser Arbeitsprozess<br><b>In 3 schritten</b></h4>
    <p>Sed ut perspiciatis unde omnis iste natus error sit voluptatem accusantium doloremque laudantium, totam rem aperiam, eaque ipsa quae ab illo inventore veritatis et quasi.</p>
    <div class="more">MEHR MEHR +</div>
  </div>
  <div class="abs step" style="left:152px;top:245px;background:var(--grey)">
    <svg width="28" height="30" viewBox="0 0 28 30" fill="none" stroke="#fff" stroke-width="1.2"><path d="M14 6a7 7 0 0 0-4 12.7V22h8v-3.3A7 7 0 0 0 14 6z"/><path d="M11 24h6M12 26.5h4M14 1v2M4 5l1.5 1.5M24 5l-1.5 1.5M1 13h2M25 13h2"/></svg>
    <h4>Planung und strategie</h4>
    <p>Sed ut perspiciatis unde omnis iste natus error sit voluptatem accusantium doloremque laudantium.</p>
  </div>
  <div class="abs step" style="left:4px;top:388px;background:var(--grey-dark)">
    <svg width="32" height="28" viewBox="0 0 32 28" fill="none" stroke="#fff" stroke-width="1.2"><path d="M7 9l-5 5 5 5M25 9l5 5-5 5M22 2L12 20l-2 5 4-3L24 4z"/></svg>
    <h4>Entwickeln</h4>
    <p>Sed ut perspiciatis unde omnis iste natus error sit voluptatem accusantium doloremque laudantium.</p>
  </div>
  <div class="abs step" style="left:152px;top:388px;background:var(--grey-dark)">
    <svg width="30" height="30" viewBox="0 0 30 30" fill="none" stroke="#fff" stroke-width="1.2"><path d="M27 3c-8 0-14 5-17 11l6 6c6-3 11-9 11-17z"/><circle cx="20" cy="10" r="2.2"/><path d="M10 14l-5 1-2 4 6-1M16 20l-1 5-4 2 1-6M8 22l-4 5M6 19l-3 3M11 24l-3 3"/></svg>
    <h4>Testen &amp; liefern</h4>
    <p>Sed ut perspiciatis unde omnis iste natus error sit voluptatem accusantium doloremque laudantium.</p>
  </div>

  <div class="abs partners-label">UNSERE PARTNER //<br>TECHNOLOGIEN VERWENDET</div>
  <div class="abs partners">
    <div class="badge" style="left:18px;top:9px;background:#e7e7e7;border-radius:50%;width:46px"></div>
    <div class="badge" style="left:77px;top:9px"></div>
    <div class="badge" style="left:139px;top:9px"></div>
    <div class="badge" style="left:14px;top:43px;background:#8f8f8f"></div>
    <div class="badge" style="left:77px;top:43px"></div>
    <div class="badge" style="left:139px;top:43px"></div>
  </div>

  <div class="abs contact">
    <h5>KONTAKTFORMULAR</h5>
    <div class="field" style="left:5px;top:38px;width:69px">Ihr Name</div>
    <div class="field" style="left:79px;top:38px;width:73px">Ihre Telefonnr</div>
    <div class="field" style="left:157px;top:38px;width:73px">Ihre Email-Adresse</div>
    <div class="field" style="left:5px;top:62px;width:294px;height:44px">Ihre Nachricht</div>
    <div class="abs btn-red send">SENDEN</div>
    <div class="foot-col" style="left:5px;top:136px;font-size:6px;font-weight:600">GET IN TOUCH</div>
    <div class="foot-col" style="left:5px;top:149px">T 0 (+49) 1234 / 5678-90<br>Email: info@korvan-systeme.de</div>
    <div class="foot-col" style="left:5px;top:168px">korvan-systeme.de<br>Am Mühlbach 5 59000 Felddorf</div>
    <div class="foot-nav">Zuhause<br>Partnernetzwerk<br>Wir über uns<br>Aktuelle Angebote<br>Zertifikate</div>
    <div class="foot-bar"></div>
    <div class="copy">© 2017 <b>KORVAN-IT</b></div>
    <div class="social"><i></i><i></i><i></i><i></i></div>
  </div>
</section>

</body>
</html>
```